Executive Education Business needs a brochure for an IT Security workshop

UPDATE AND CLARIFICATION - I'm looking for a brochure that includes the text from the attached file "2014 IT Security Program Outline v2". This is a specific program we are putting on that we need a brochure designed for, using the content included in this file.

We have the basic text of a brochure, and need a design layout for a brochure that we can use to market this workshop to financial institutions in Asia and the Middle East. It may make sense to leave a spot on the cover somewhere to add a location and date (which we can edit based on program scheduling). Additionally, a registration page should be included either in the brochure or as an insert.

I'm attaching a brochure we used for a past program which provides an example registration page for our programs. I'm also including some photos from our programs that may be of use, although stock photography is also acceptable. Finally, I'm including two of our corporate brochures that may provide additional background on the company and our style.

```html
<!DOCTYPE html>
<html lang="en">
<head>
<meta charset="utf-8">
<title>IT Security Program Brochure</title>
<link href="https://fonts.googleapis.com/css2?family=Source+Sans+3:wght@300;400;600;700&display=swap" rel="stylesheet">
<style>
:root{
  --backdrop:#2a2a2a;
  --paper:#ffffff;
  --faculty-bg:#e3e3e3;
  --agenda-bg-a:#f4f4f4;
  --agenda-bg-b:#cfcfcf;
  --band:#6b6b6b;
  --ink:#1d1d1d;
  --heading:#4a4a4a;
  --body:#666666;
  --rule:#c4c4c4;
  --photo-a:#6e4a2c;
  --photo-b:#2c2622;
  --portrait:#9a9a9a;
}
*{margin:0;padding:0;box-sizing:border-box}
html,body{width:1200px;height:793px;overflow:hidden;background:var(--backdrop)}
body{font-family:"Source Sans 3",Arial,sans-serif;position:relative}
.spread{position:absolute;left:193px;top:90px;width:857px;height:607px;background:var(--paper);overflow:hidden}
.page-left{position:absolute;left:0;top:0;width:428px;height:607px;background:var(--paper)}
.page-right{position:absolute;left:428px;top:0;width:429px;height:607px;background:linear-gradient(90deg,var(--agenda-bg-b) 0%,var(--agenda-bg-a) 12%,#ededed 70%,#dedede 100%)}
.event-photo{position:absolute;left:0;top:25px;width:857px;height:153px;background:linear-gradient(180deg,#8a6a48 0%,var(--photo-a) 35%,var(--photo-b) 100%)}
.brand{position:absolute;right:18px;top:46px;display:flex;align-items:center;gap:6px;color:#fff;font-size:14px;font-weight:300;letter-spacing:.2px}
.brand-dot{width:13px;height:13px;border:1px solid #fff;border-radius:50%}
.web{position:absolute;right:10px;top:160px;color:#fff;font-size:7.5px}

.intro{position:absolute;left:0;top:183px;width:428px;height:107px}
.intro-title{position:absolute;left:27px;top:4px;width:135px;font-size:10.5px;font-weight:400;line-height:12.5px;color:var(--ink)}
.intro-text{position:absolute;left:27px;top:44px;width:130px;font-size:6.8px;line-height:8.2px;color:var(--ink)}
.intro-list{position:absolute;left:160px;top:2px;width:122px;list-style:none;font-size:5.8px;line-height:6.8px;color:var(--ink)}
.intro-list li{margin-bottom:2.6px}
.intro-list li::before{content:"• "}
.intro-note{position:absolute;left:287px;top:2px;width:124px;font-size:5.8px;line-height:6.8px;color:var(--ink)}

.faculty{position:absolute;left:0;top:290px;width:428px;height:317px;background:var(--faculty-bg)}
.faculty-label{position:absolute;left:27px;top:3px;font-size:14px;font-weight:300;color:var(--heading)}
.faculty-line{position:absolute;left:0;top:24px;width:428px;height:1px;background:var(--rule)}
.member{position:absolute;top:32px;width:122px;height:280px}
.member+.member{border-left:1px solid var(--rule)}
.member-1{left:27px}
.member-2{left:150px;padding-left:12px;width:134px}
.member-3{left:285px;padding-left:12px;width:134px}
.portrait{width:62px;height:62px;border-radius:50%;background:radial-gradient(circle at 50% 40%,#bdbdbd,var(--portrait) 60%,#5d5d5d);margin:0 0 0 25px;border:2px solid #fff}
.member-name{margin-top:25px;font-size:10.5px;font-weight:700;color:var(--ink);line-height:12px}
.member-bio{font-size:6.6px;line-height:8.1px;color:var(--ink)}

.agenda-band{position:absolute;left:0;top:182px;width:429px;height:26px;background:var(--band);color:#fff;font-size:19px;font-weight:300;padding-left:25px;line-height:26px}
.session{position:absolute;width:185px}
.col-1{left:25px}
.col-2{left:222px}
.s1{top:218px}.s2{top:339px}.s3{top:466px}
.s-cont{top:218px}.s4{top:331px}.s5{top:513px}
.session-no{font-size:10px;font-weight:700;color:var(--heading);line-height:11px}
.session-title{font-size:9.5px;font-weight:300;color:var(--heading);line-height:10.5px;margin-bottom:2px}
.s1 .session-title{margin-bottom:10px}
.session p{font-size:6.6px;line-height:8.1px;color:var(--body)}
</style>
</head>
<body>
<main class="spread">
  <section class="page-left">
    <div class="intro">
      <h1 class="intro-title">IT Security: Protecting the Integrity of your Technology Platforms</h1>
      <p class="intro-text">This one-day course, specifically designed for senior executives and IT professionals with direct responsibility for protecting the integrity of technology platforms, will enhance your understanding of the challenges faced by today's IT workforce. Key areas of discussion will include:</p>
      <ul class="intro-list">
        <li>Identifying unusual or unauthorized activity, breaches, or attempted access.</li>
        <li>Safeguards against outside intrusion.</li>
        <li>Building a framework of security controls and policies.</li>
        <li>Internal reporting and controls.</li>
        <li>Risks presented by embedded systems and mobile devices.</li>
        <li>Human resource considerations and reducing dependencies on individuals with key IT knowledge.</li>
        <li>Disaster recovery best practices, procedures, systems, and operating protocols.</li>
      </ul>
      <p class="intro-note"><strong>Mr. Karim J. Haddad</strong>, Chairman of Halden Institute of Executive Studies, will lead a panel of experts with extensive industry experience in what promises to be a relevant and engaging program. In addition to learning from our senior faculty members, participants will be encouraged to share their own insights with the group about emerging best practices.</p>
    </div>
    <div class="faculty">
      <h2 class="faculty-label">Faculty</h2>
      <div class="faculty-line"></div>
      <article class="member member-1">
        <div class="portrait" role="img" aria-label="Portrait photo of Karim J. Haddad"></div>
        <h3 class="member-name">Karim J. Haddad</h3>
        <p class="member-bio">is Chairman of Halden Institute of Executive Studies and a faculty member for the RFLC, where he teaches in the Board Governance Leadership Programme (BGLP).<br>Mr. Haddad recently served as Professor of Management Practice at Eastbrook Business School, where he taught courses in corporate governance, corporate finance, and private equity finance, among other subject matters.<br>In addition, Mr. Haddad has direct private equity investing and operating experience with Crestline Partners and as Chairman and CEO of an operating company for nearly 10 years. He has taught and consulted for leading financial institutions and currently serves on five boards of directors.</p>
      </article>
      <article class="member member-2">
        <div class="portrait" role="img" aria-label="Portrait photo of Laurent Mercier"></div>
        <h3 class="member-name">Laurent Mercier</h3>
        <p class="member-bio">knows how banks work from the inside. He has run the operations and information technology of banks including Northgate Bank, Westmere Capital and most recently was the Chief Operating Officer of Gulfstar Commercial Bank.<br>His experience in running middle and back office operations and IT, often involving complex derivative products, gives him a practical understanding of operational risk management.<br>He is a French National and graduated from the École de Commerce de Valmont. He is a qualified "Expert Comptable Mémorialiste" (French ACA) and began his career as an auditor with Abbott and Lowe.</p>
      </article>
      <article class="member member-3">
        <div class="portrait" role="img" aria-label="Portrait photo of Leila Nassar"></div>
        <h3 class="member-name">Leila Nassar</h3>
        <p class="member-bio">is an independent Information Security consultant and has co-authored several articles and patents in the fields of embedded security, cryptography, intrusion detection, cyber physical systems, and Operating Systems security.<br>She is also a Senior Associate at Harlow &amp; Company, serving large corporate clients in the information and communications technology industry, with a focus on information security and risk management, information governance, corporate strategy, and corporate governance.<br>She holds a Ph.D. in Information Security from Kestrel University, and has served clients in the USA, the Middle East, Australia, Africa, and Asia.</p>
      </article>
    </div>
  </section>

  <section class="page-right">
    <h2 class="agenda-band">Program Agenda</h2>
    <div class="session col-1 s1">
      <h3 class="session-no">Session 1</h3>
      <h4 class="session-title">IT Security Management</h4>
      <p>We open our program by examining the issue of IT security and its increasing importance in today's increasingly connected world. Using a fictional case describing an IT security breach, we discuss the risk management aspects of IT, the cost-benefit tradeoffs of managing these risks, and the role of the Risk Management in preparing for and managing a crisis situation. We also examine how hackers gain access to systems with the unwitting assistance of well-meaning employees and discuss the implications of these findings for system and security design.</p>
    </div>
    <div class="session col-1 s2">
      <h3 class="session-no">Session 2</h3>
      <h4 class="session-title">Information Governance Frameworks</h4>
      <p>In the course of their operations, organizations across all industry sectors create, process, and use sensitive information and data in need of protection. Information Security is therefore a major concern to any organization, serving to protect its information assets, mitigate security attacks, ensure competitiveness, and maintain brand image and equity.<br>This session addresses the need of organizations to build assets and information inventories, classify such inventories, and build a framework of security controls and policies across all levels of an organization based on exposure to vulnerability exploits, cyber threats, and associated risks.</p>
    </div>
    <div class="session col-1 s3">
      <h3 class="session-no">Session 3</h3>
      <h4 class="session-title">Embedded Systems and Security</h4>
      <p>Embedded systems are ubiquitously used to capture, store, and manipulate data of a sensitive nature (e.g., personal appliances, such as cell phones, tablets, smart cards, portable storage devices, wireless handsets, networked sensors, etc.), or perform safety-critical functions (e.g., automotive and aviation electronics, medical appliances, etc.). As these systems become increasingly complex and connected, with the ability to connect to and download programs from public networks, security becomes a serious concern in their design.</p>
    </div>
    <div class="session col-2 s-cont">
      <p>A straightforward method to achieving security requirements would be to adapt security approaches designed for general-purpose systems. However, this generally falls because of the various challenges and bottlenecks faced during the design process of their embedded counterparts. These challenges include: (i) processing gap; (ii) battery gap; (iii) tamper resistance; (iv) flexibility; and (v) cost.<br><br>This session addresses challenges caused by resource embedded system constraints (in particular mobile devices) and implications for organizations and employees. We also present and review various innovations and solutions for mitigating such challenges.</p>
    </div>
    <div class="session col-2 s4">
      <h3 class="session-no">Session 4</h3>
      <h4 class="session-title">Risk Management and Business Continuity Planning</h4>
      <p>"A chain is only as strong as its weakest link." In other words, a security solution is only as strong as its most vulnerable area. Unfortunately, experience has shown that people are often the weakest link in a security chain.<br>In this session we address the personal aspects of IT Security and how technical solutions can be put at risk if an organization does not have the appropriate risk culture or adequate risk awareness. We will identify key areas of "people risk" and describe best practices for system design that take these human factors into account.<br>Additionally, we will discuss various IT operational risks, business continuity planning, and disaster recovery. In particular, we will focus on the roles and responsibilities required in managing these risks and will outline practical lessons for Board members, senior management, and IT professionals in working together to minimize the impact of operational risks.</p>
    </div>
    <div class="session col-2 s5">
      <h3 class="session-no">Session 5</h3>
      <h4 class="session-title">Panel Discussion</h4>
      <p>The program will conclude with a panel discussion on topics such as crisis management, organizational preparedness, and risk management implications. Particular emphasis will be placed on identifying practical lessons for program participants, and our panel of experts will welcome questions from the audience.</p>
    </div>
  </section>

  <div class="event-photo" role="img" aria-label="Photo of a speaker addressing a full seminar room of seated participants"></div>
  <div class="brand"><span class="brand-dot"></span><span>Halden Institute of Executive Studies</span></div>
  <div class="web">www.haldenexec.com</div>
</main>
</body>
</html>
```